Packaging Design Project For Chocolate Brand

We need a fresh, vibrant and colourful packaging for our healthy chocolate brand, oTakeFernubrio.

WHAT IS oTakeFernubrio?

oTakeFernubrio are indulgent chocolates that help reduce your body weight by controlling your appetite and calorie intake. And the best thing is that it tastes 100% genuine chocolate, only healthier.

WHAT WE NEED FROM YOU

Although we have collected a few logos from other designers, it's not quite catchy to the eye. As it will appear on retail shelves, it needs to catch the eye. It's up to the designers if they want to design the logo all in one word or two words. We will provide feedback quickly. We are contemplating on a sub-title beneath the logo, with the words "Unwrap. Eat. Lose." It is the main logo "oTakeFernubrio" that needs to stand out though with possibly some chocolatey or slimming/dieting aspect. However we do not want any images of thin bodies around the logo. Use of imagination involving chocolate could be beneficial, e.g. melting chocolate etc.
Use different colours for 'i', 'Love', and 'Fernubrio'. Maybe include an illustration around the logo if you feel it will brighten the brand.

Packaging

Although we do not have a specific theme in mind, the designer may want to try a retro look with illustrations/images, funky, maybe professional but keep it modern and looking like a chocolate bar.

Dimensions - 155mm(width) x 76.8mm(height) x 34mm(depth)
Portrait or landscape. Designers choice.

There are three flavours, Milk, White and Dark so three different packages with different colours. The rest of the packages will look more or less the same. The packaging itself needs 'wavey' aspects of chocolate. Wavey, circular, elegant shapes which appeal to the eye

There are certain texts which need to go on the front end of the box. The designer has the option of using 2 different texts in their work to come up with the best design. Texts are on the files. More text may be added but in the meantime please use what is given.
Updates

Project Deadline Extended
Reason: Hi, The deadline has been extended a further 7 days for those who designers who started their designs late are concerned about the timeframe. So there is no need to rush your designs. I hope the 7 days extension is enough for those that need it. Many thanks,

Target Market(s)

Women aged 16-45, C1C2 class

Industry/Entity Type

Landscape

Requirements
Must have
• Appealing mostly to women aged 16-45, C1C2 class.
Colourful
Chocolatey feel with wavey lines etc
Strong Logo
Nice to have
• It can come across as a food supplement that you normally see on the pharmacy shelf but with an unconventional design twist. Or the designer may think it will not work and for it to have the chocolatey feel, there cannot be any connection a pharmaceutical package. It has to remain like a regular chocolate bar that you see in the supermarket. Up to the designer to choose. It will be going into both supermarket stores and healthfood stores.

The designer should have some personal input in the design. If you were browsing around the supermarket and spotted it, would you stop and look at it? If not, the design will need changing.

Secondly, maybe a brand illustration would go well with the logo. Possibly an animal illustration relating to chocolate (somehow) or simply a chocolate with a measuring tape around it getting slimmer and slimmer. Just a few thoughts

```html
<!DOCTYPE html>
<html lang="en">
<head>
<meta charset="utf-8">
<title>oTakeFernubrio – Chocolate Packaging Range</title>
<link rel="stylesheet" href="https://fonts.googleapis.com/css2?family=Comfortaa:wght@300;700&family=Dancing+Script:wght@600&display=swap">
<style>
  :root {
    --stage-dark: #140c07;
    --stage-mid: #2e1e14;
    --wrapper-cream: #efe7d5;
    --wrapper-stripe: #e6ddc8;
    --wrapper-edge: #cdbf9f;
    --ink-dark: #2a1d16;
    --ink-body: #4a3a30;
    --ink-script: #7a3b22;
    --logo-white: #fbf6ec;
    --purple: #6b2384;
    --purple-deep: #3e0f50;
    --maroon: #6d1a1d;
    --maroon-deep: #3d0b0d;
    --navy: #1f3142;
    --navy-deep: #0f1a25;
  }
  * { box-sizing: border-box; margin: 0; padding: 0; }
  html, body { width: 1200px; height: 918px; overflow: hidden; }
  body {
    background: radial-gradient(ellipse at 50% 35%, var(--stage-mid), var(--stage-dark) 75%);
    font-family: "Comfortaa", sans-serif;
    position: relative;
  }
  .range { position: absolute; inset: 0; }
  .pack {
    position: absolute;
    top: 80px;
    width: 300px;
    height: 740px;
    background:
      repeating-linear-gradient(90deg, var(--wrapper-cream) 0 6px, var(--wrapper-stripe) 6px 8px);
    border: 2px solid var(--wrapper-edge);
    box-shadow: 0 10px 30px rgba(0,0,0,.6), inset 0 0 0 6px rgba(255,255,255,.25), inset 0 0 24px rgba(120,90,50,.35);
  }
  .pack--milk-purple { left: 98px;  --tone: var(--purple); --tone-deep: var(--purple-deep); }
  .pack--milk-maroon { left: 430px; --tone: var(--maroon); --tone-deep: var(--maroon-deep); }
  .pack--milk-navy   { left: 762px; --tone: var(--navy);   --tone-deep: var(--navy-deep); }

  .pack__banner { position: absolute; left: 16px; top: 0; width: 268px; height: 206px; }
  .pack__banner-shape { fill: var(--tone); }
  .pack__banner-shade { fill: var(--tone-deep); opacity: .45; }
  .pack__brand {
    position: absolute; left: 16px; top: 98px; width: 268px;
    text-align: center;
    font-weight: 700; font-size: 38px; letter-spacing: -0.5px;
    color: var(--logo-white);
  }
  .pack__tagline {
    position: absolute; left: 0; right: 0; top: 240px;
    text-align: center;
    font-weight: 700; font-size: 19px; color: var(--ink-dark);
  }
  .pack__photo {
    position: absolute; left: 54px; top: 300px; width: 192px; height: 140px;
    background: radial-gradient(ellipse at 50% 55%, #6a4330 0 28%, var(--tone) 58%, var(--tone-deep));
    box-shadow: 0 2px 6px rgba(0,0,0,.35);
  }
  .pack__flavour {
    position: absolute; left: 0; right: 0; top: 456px;
    text-align: center;
    font-weight: 300; font-size: 21px; color: var(--ink-body);
  }
  .pack__claim {
    position: absolute; left: 34px; right: 34px; top: 512px;
    text-align: center;
    font-weight: 700; font-size: 10.5px; line-height: 15px; color: var(--ink-body);
  }
  .pack__descriptor {
    position: absolute; left: 0; right: 0; top: 582px;
    text-align: center;
    font-family: "Dancing Script", cursive; font-weight: 600; font-size: 22px;
    color: var(--ink-script);
  }
  .pack__weight {
    position: absolute; left: 100px; top: 632px; width: 100px; height: 58px;
    background: var(--tone);
    color: var(--logo-white);
    text-align: center;
    font-size: 12.5px; line-height: 17px;
    padding-top: 12px;
  }
</style>
</head>
<body>
<main class="range">

  <section class="pack pack--milk-purple">
    <svg class="pack__banner" viewBox="0 0 268 206" aria-hidden="true">
      <polygon class="pack__banner-shade" points="0,0 268,0 268,150 134,206 0,150"/>
      <polygon class="pack__banner-shape" points="10,0 258,0 258,142 134,196 10,142"/>
    </svg>
    <p class="pack__brand">Fernubrio!</p>
    <p class="pack__tagline">Unwrap. Eat. Lose.</p>
    <div class="pack__photo" role="img" aria-label="Photo of broken milk chocolate pieces with shavings"></div>
    <p class="pack__flavour">Milk Chocolate Flavoured</p>
    <p class="pack__claim">oTakeFernubrio are indulgent chocolates that help reduce your body weight by controlling your appetite and calorie intake.</p>
    <p class="pack__descriptor">Rich &amp; Creamy</p>
    <p class="pack__weight">Net. Wgt.<br>86g @ 4oz</p>
  </section>

  <section class="pack pack--milk-maroon">
    <svg class="pack__banner" viewBox="0 0 268 206" aria-hidden="true">
      <polygon class="pack__banner-shade" points="0,0 268,0 268,150 134,206 0,150"/>
      <polygon class="pack__banner-shape" points="10,0 258,0 258,142 134,196 10,142"/>
    </svg>
    <p class="pack__brand">Fernubrio!</p>
    <p class="pack__tagline">Unwrap. Eat. Lose.</p>
    <div class="pack__photo" role="img" aria-label="Photo of broken milk chocolate pieces with shavings"></div>
    <p class="pack__flavour">Milk Chocolate Flavoured</p>
    <p class="pack__claim">oTakeFernubrio are indulgent chocolates that help reduce your body weight by controlling your appetite and calorie intake.</p>
    <p class="pack__descriptor">Rich &amp; Creamy</p>
    <p class="pack__weight">Net. Wgt.<br>86g @ 4oz</p>
  </section>

  <section class="pack pack--milk-navy">
    <svg class="pack__banner" viewBox="0 0 268 206" aria-hidden="true">
      <polygon class="pack__banner-shade" points="0,0 268,0 268,150 134,206 0,150"/>
      <polygon class="pack__banner-shape" points="10,0 258,0 258,142 134,196 10,142"/>
    </svg>
    <p class="pack__brand">Fernubrio!</p>
    <p class="pack__tagline">Unwrap. Eat. Lose.</p>
    <div class="pack__photo" role="img" aria-label="Photo of broken milk chocolate pieces with shavings"></div>
    <p class="pack__flavour">Milk Chocolate Flavoured</p>
    <p class="pack__claim">oTakeFernubrio are indulgent chocolates that help reduce your body weight by controlling your appetite and calorie intake.</p>
    <p class="pack__descriptor">Rich &amp; Creamy</p>
    <p class="pack__weight">Net. Wgt.<br>86g @ 4oz</p>
  </section>

</main>
</body>
</html>
```